Design for web app with Brindle Surface System - Tarvo7 SMS consult

We are developing a web app that will work in browsers. Its main purpose is to allow for users (signing up and logging in with their phone number) to track their habbits and select consultants to whom they can send SMS for help.

The wireframes of the app can be accessed here (pdf):
https://files.quellbox.example/d/7Kx2PmR9vTq4LnZ8wYs3HbJ6cFe1/view?usp=sharing

NB!: Please do not follow the mockups 100% literally, but the Brindle Surface system guidelines.

The technical specifications and descriptions of the web app's functionalities are available in the link below:
https://pages.quellbox.example/document/d/4TrNk8WqZp2LmVx7YcBs9HdJ3fRe6GaU1oKi5QeXtwy0/edit?usp=sharing

Requirements for the design:

- The design should be provided as PSD, where each page/section should be in its own PSD file OR all pages/sections should be represented as folder groups in a single PSD file.

- All graphical elements in the design should be delivered as single layers which can then be extracted from the PSD.

- All graphical elements (icons, graphical buttons, etc.) should be provided as vector objects in the PSD, so that they can be exported into different sizes without loss of quality (for responsiveness).

- The design should use either web safe fonts or Brindle Type.

Instructions for the design:
The design should be based on Brindle Surface System - http://www.brindle.example/design/spec/surface-system/introduction.html

Please also provide an app icon and suggest a logo for the app.

• Based on Brindle Surface System
• Flat
• Nice looking and not so stiff as the default Brindle Surface System, but it is important to follow their guidelines.
• 3D

```html
<!DOCTYPE html>
<html lang="en">
<head>
<meta charset="utf-8">
<title>Tarvo7 – Sign up</title>
<link rel="stylesheet" href="https://fonts.googleapis.com/css2?family=Montserrat:wght@500;600&family=Roboto:wght@400&display=swap">
<style>
  :root {
    --bar-blue: #0a72aa;
    --screen-dark: #27323f;
    --screen-dark-deep: #222c38;
    --screen-haze: #34414f;
    --field-white: #ffffff;
    --icon-grey: #9a9ea8;
    --placeholder-grey: #aeb1c0;
    --primary-blue: #2360b8;
    --cancel-coral: #ff6467;
    --text-white: #ffffff;
    --logo-tile: #0b6fa6;
  }
  * { margin: 0; padding: 0; box-sizing: border-box; }
  html, body { width: 676px; height: 1200px; overflow: hidden; background: var(--screen-dark); }
  .screen {
    position: relative; width: 676px; height: 1200px; overflow: hidden;
    font-family: "Roboto", Arial, sans-serif; color: var(--text-white);
  }
  .backdrop {
    position: absolute; left: 0; top: 147px; width: 676px; height: 1053px;
    background:
      radial-gradient(ellipse 260px 340px at 470px 210px, var(--screen-haze) 0%, rgba(52,65,79,0) 100%),
      radial-gradient(ellipse 200px 260px at 90px 120px, rgba(52,65,79,0.7) 0%, rgba(52,65,79,0) 100%),
      linear-gradient(180deg, var(--screen-dark) 0%, var(--screen-dark-deep) 100%);
  }
  .status-bar {
    position: absolute; left: 0; top: 0; width: 676px; height: 42px;
    background: var(--bar-blue); font-size: 21px; line-height: 42px;
  }
  .status-bar .signal { position: absolute; left: 12px; top: 15px; display: flex; gap: 3px; }
  .status-bar .signal span { width: 11px; height: 11px; border-radius: 50%; border: 1.5px solid var(--text-white); }
  .status-bar .signal span.on { background: var(--text-white); }
  .status-bar .carrier { position: absolute; left: 94px; top: 0; }
  .status-bar .wifi { position: absolute; left: 164px; top: 11px; }
  .status-bar .time { position: absolute; left: 0; width: 676px; text-align: center; top: 0; font-weight: 500; }
  .status-bar .bt { position: absolute; left: 510px; top: 10px; }
  .status-bar .charge { position: absolute; left: 541px; top: 0; }
  .status-bar .battery { position: absolute; left: 612px; top: 12px; }
  .nav-bar {
    position: absolute; left: 0; top: 42px; width: 676px; height: 105px; background: var(--bar-blue);
  }
  .nav-bar .back { position: absolute; left: 62px; top: 42px; }
  .nav-bar .title {
    position: absolute; left: 0; width: 676px; top: 0; line-height: 105px;
    text-align: center; font-size: 31px; font-weight: 400;
  }
  .brand {
    position: absolute; left: 153px; top: 248px; height: 58px;
    display: flex; align-items: center; gap: 14px;
  }
  .brand .tile { width: 20px; height: 20px; background: var(--logo-tile); }
  .brand .name {
    font-family: "Montserrat", Arial, sans-serif; font-weight: 500; font-size: 44px;
    color: var(--text-white); letter-spacing: 1px;
  }
  .phone-field {
    position: absolute; left: 0; top: 487px; width: 676px; height: 106px;
    background: var(--field-white);
  }
  .phone-field .icon { position: absolute; left: 37px; top: 34px; }
  .phone-field .placeholder {
    position: absolute; left: 132px; top: 0; line-height: 106px;
    font-size: 34px; color: var(--placeholder-grey);
  }
  .button {
    position: absolute; left: 58px; width: 555px; height: 105px; border-radius: 3px;
    font-family: "Montserrat", Arial, sans-serif; font-weight: 600; font-size: 31px;
    letter-spacing: 1px; text-align: center; line-height: 105px; color: var(--text-white);
  }
  .button.sign-up { top: 693px; background: var(--primary-blue); }
  .button.cancel { top: 1049px; left: 59px; background: var(--cancel-coral); }
</style>
</head>
<body>
<main class="screen">
  <div class="backdrop" role="img" aria-label="Dark blue background with a faint silhouette of a person in profile"></div>

  <header class="status-bar">
    <div class="signal"><span class="on"></span><span class="on"></span><span class="on"></span><span></span><span></span></div>
    <span class="carrier">KESTA</span>
    <svg class="wifi" width="24" height="20" viewBox="0 0 24 20" fill="none" stroke="#fff" stroke-width="2.4" stroke-linecap="round">
      <path d="M2 7a14 14 0 0 1 20 0"/><path d="M6 11a8.5 8.5 0 0 1 12 0"/><circle cx="12" cy="16" r="1.8" fill="#fff" stroke="none"/>
    </svg>
    <span class="time">4:21 PM</span>
    <svg class="bt" width="16" height="24" viewBox="0 0 16 24" fill="none" stroke="#8fb4cf" stroke-width="1.8" stroke-linejoin="round">
      <path d="M2 6l12 11-6 5V2l6 5L2 18"/>
    </svg>
    <span class="charge">100%</span>
    <svg class="battery" width="52" height="20" viewBox="0 0 52 20">
      <rect x="1" y="1" width="45" height="18" rx="3" fill="none" stroke="#fff" stroke-width="1.6"/>
      <rect x="3.5" y="3.5" width="40" height="13" rx="1.5" fill="#fff"/>
      <rect x="47.5" y="6.5" width="3" height="7" rx="1" fill="#fff"/>
    </svg>
  </header>

  <nav class="nav-bar">
    <svg class="back" width="18" height="28" viewBox="0 0 18 28" fill="none" stroke="#fff" stroke-width="3.4" stroke-linecap="round" stroke-linejoin="round">
      <path d="M14 4L5 14l9 10"/>
    </svg>
    <h1 class="title">Sign up</h1>
  </nav>

  <div class="brand">
    <span class="name">Tarvo7</span>
    <span class="tile"></span>
  </div>

  <label class="phone-field">
    <svg class="icon" width="38" height="38" viewBox="0 0 24 24" fill="none" stroke="var(--icon-grey)" stroke-width="1" stroke-linejoin="round">
      <path d="M6.6 2.5l2.6 4.1c.3.5.2 1.1-.2 1.5L7.6 9.4c1.2 2.9 3.9 5.7 7 7l1.3-1.4c.4-.4 1-.5 1.5-.2l4.1 2.6c.5.3.7 1 .4 1.5l-1.3 2.2c-.5.8-1.4 1.2-2.3 1C10.8 20.6 3.4 13.2 1.9 5.6c-.2-.9.2-1.8 1-2.3l2.2-1.3c.5-.3 1.2-.1 1.5.5z"/>
    </svg>
    <span class="placeholder">phone</span>
  </label>

  <div class="button sign-up">SIGN UP</div>
  <div class="button cancel">CANCEL</div>
</main>
</body>
</html>
```